Corporate Design für Tische aus hochwertigen Hölzern
Zielgruppe
Ich fertige Tische aus hochwertigen Hölzern in Kombination mit Epoxidharz und Metallgestellen. Meine Zielgruppe sind Mann und Frau mittleren bis älteren Alters mit einem Bewusstsein für handgefertigte Unikate.
Aufgabenstellung
Sehr geehrte Künstlerinnen und Künstler, ich bin auf der Suche nach einem Design, welches relativ schlicht gehalten ist aber eine deutliche Verknüpfung zu meiner Arbeit herstellt. Das Design sollte Luxus, Einzigartigkeit, Exklusivität und Handwerkskunst vermitteln. Das Logo sollte aus meinem Namen und einem Bild welches den Kernpunkt meiner Arbeit (exklusive Möbel, meistens Tische) wiederspiegelt bestehen. Das letzte Wort in der Namensfindung ist noch nicht gesprochen, Sie können gerne auch einen eigenen Vorschlag erbringen. Ich bin sehr gespannt und neugierig auf Ihre Vorschläge. PS: Der Gewinner wird als Folgeauftrag noch für das Erstellen einer Broschüre engagiert und in naher Zukunft wird auch noch ein passender Web-Auftritt benötigt.

```html
<!DOCTYPE html>
<html lang="de">
<head>
<meta charset="utf-8">
<title>Marlen Voskuhl – Exclusive Wood Design</title>
<link href="https://fonts.googleapis.com/css2?family=Montserrat:wght@400;500&family=Arimo:wght@400&family=Exo+2:wght@400;500;700&display=swap" rel="stylesheet">
<style>
  :root {
    --ink: #4d4d4f;
    --gold: #c98f3f;
    --gold-light: #ecc89a;
    --paper: #ffffff;
    --stage: #ece7e2;
    --body: #6b6b6d;
    --slate: #55565a;
  }
  * { margin: 0; padding: 0; box-sizing: border-box; }
  html, body { width: 1192px; height: 1200px; overflow: hidden; }
  body { position: relative; background: var(--paper); font-family: "Arimo", Arial, sans-serif; }

  .brand-row { position: absolute; top: 0; left: 0; width: 1192px; height: 322px; background: var(--paper); }
  .lockup { position: absolute; text-align: center; }
  .lockup--left { left: 43px; top: 185px; width: 560px; }
  .lockup--right { left: 600px; top: 181px; width: 560px; }
  .wordmark { font-family: "Montserrat", sans-serif; font-weight: 400; color: var(--ink); letter-spacing: 0.06em; white-space: nowrap; }
  .lockup .wordmark { font-size: 43px; }
  .tagline { font-family: "Montserrat", sans-serif; font-weight: 400; color: var(--ink); letter-spacing: 0.28em; white-space: nowrap; }
  .lockup .tagline { font-size: 17px; margin-top: 10px; }
  .tagline--gold { color: var(--gold); font-weight: 500; }

  .stage { position: absolute; top: 322px; left: 0; width: 1192px; height: 878px; background: var(--stage); }

  .gold-bar { position: absolute; top: 0; left: 0; background: linear-gradient(90deg, var(--gold-light), var(--gold) 60%, var(--gold-light)); }
  .slate-bar { position: absolute; bottom: 0; right: 0; background: var(--slate); }

  .letterhead { position: absolute; left: 160px; top: 81px; width: 490px; height: 692px; background: var(--paper); box-shadow: 0 2px 6px rgba(0,0,0,0.15); }
  .letterhead .gold-bar { width: 279px; height: 9px; }
  .letterhead .slate-bar { left: 47px; height: 9px; }
  .letterhead__brand { position: absolute; right: 66px; top: 75px; text-align: center; }
  .letterhead__brand .wordmark { font-size: 15px; }
  .letterhead__brand .tagline { font-size: 6px; margin-top: 4px; letter-spacing: 0.3em; }
  .letter { position: absolute; left: 47px; width: 360px; color: var(--body); font-size: 7.4px; line-height: 9.4px; }
  .letter--sender { top: 124px; font-size: 5px; }
  .letter--recipient { top: 143px; }
  .letter--subject { top: 190px; }
  .letter--salutation { top: 218px; }
  .letter--body { top: 237px; width: 350px; }
  .letter--closing { top: 530px; }
  .letter--signature { top: 558px; }
  .letter-footer-rule { position: absolute; left: 47px; top: 637px; width: 374px; height: 1px; background: linear-gradient(90deg, var(--gold), var(--gold-light)); }
  .letter-footer { position: absolute; top: 646px; left: 47px; display: flex; font-size: 4.3px; line-height: 5.4px; color: var(--body); font-family: "Montserrat", sans-serif; }
  .letter-footer div:nth-child(1) { width: 81px; }
  .letter-footer div:nth-child(2) { width: 77px; }
  .letter-footer div:nth-child(3) { width: 76px; }

  .card { position: absolute; left: 729px; width: 303px; height: 189px; box-shadow: 0 2px 6px rgba(0,0,0,0.15); }
  .card--front { top: 188px; background: var(--paper); font-family: "Exo 2", sans-serif; color: #333; }
  .card--front .gold-bar { width: 177px; height: 6px; }
  .card--front .slate-bar { left: 43px; height: 6px; }
  .card__brand { position: absolute; left: 150px; top: 49px; width: 145px; text-align: center; }
  .card__brand .wordmark { font-size: 10px; }
  .card__brand .tagline { font-size: 4px; margin-top: 3px; }
  .card__name { position: absolute; left: 43px; top: 74px; font-weight: 700; font-size: 9.5px; color: var(--gold); }
  .card__title { position: absolute; left: 43px; top: 87px; font-size: 5.5px; }
  .card__address { position: absolute; left: 43px; top: 115px; font-size: 7px; line-height: 12px; }
  .card__contacts { position: absolute; left: 188px; top: 115px; font-size: 7px; line-height: 12px; list-style: none; }
  .card__contacts li { display: flex; align-items: center; gap: 5px; }
  .card__contacts svg { width: 8px; height: 8px; }

  .card--back { top: 443px; background: var(--slate); display: flex; align-items: center; justify-content: center; }
  .card--back .wordmark { color: var(--paper); font-size: 17px; }
</style>
</head>
<body>
  <section class="brand-row">
    <div class="lockup lockup--left">
      <div class="wordmark">MARLEN VOSKUHL</div>
      <div class="tagline">EXCLUSIVE WOOD DESIGN</div>
    </div>
    <div class="lockup lockup--right">
      <div class="wordmark">MARLEN VOSKUHL</div>
      <div class="tagline tagline--gold">EXCLUSIVE WOOD DESIGN</div>
    </div>
  </section>

  <section class="stage">
    <article class="letterhead">
      <div class="gold-bar"></div>
      <div class="letterhead__brand">
        <div class="wordmark">MARLEN VOSKUHL</div>
        <div class="tagline">EXCLUSIVE WOOD DESIGN</div>
      </div>
      <p class="letter letter--sender">Max Mustermann Beispielstraße 38 12345 Beispielort</p>
      <p class="letter letter--recipient">Beispielfirma GmbH<br>Firmenstraße 12<br>12345 Firmenort</p>
      <p class="letter letter--subject">Betreffzeile</p>
      <p class="letter letter--salutation">Sehr geehrte Damen und Herren,</p>
      <p class="letter letter--body">Lorem ipsum dolor sit amet, consetetur sadipscing elitr, sed diam nonumy eirmod tempor invidunt ut labore et dolore magna aliquyam erat, sed diam voluptua. At vero eos et accusam et justo duo dolores et ea rebum. Stet clita kasd gubergren, no sea takimata sanctus est Lorem ipsum dolor sit amet. Lorem ipsum dolor sit amet, consetetur sadipscing elitr, sed diam nonumy eirmod tempor invidunt ut labore et dolore magna aliquyam erat, sed diam voluptua. At vero eos et accusam et justo duo dolores et ea rebum. Stet clita kasd gubergren, no sea takimata sanctus est Lorem ipsum dolor sit amet. Lorem ipsum dolor sit amet, consetetur sadipscing elitr, sed diam nonumy eirmod tempor invidunt ut labore et dolore magna aliquyam erat, sed diam voluptua. At vero eos et accusam et justo duo dolores et ea rebum. Stet clita kasd gubergren, no sea takimata sanctus est Lorem ipsum dolor sit amet.<br>Duis autem vel eum iriure dolor in hendrerit in vulputate velit esse molestie consequat, vel illum dolore eu feugiat nulla facilisis at vero eros et accumsan et iusto odio dignissim qui blandit praesent luptatum zzril delenit augue duis dolore te feugait nulla facilisi. Lorem ipsum dolor sit amet, consectetuer adipiscing elit, sed diam nonummy nibh euismod tincidunt ut laoreet dolore magna aliquam erat volutpat.<br>Ut wisi enim ad minim veniam, quis nostrud exerci tation ullamcorper suscipit lobortis nisl ut aliquip ex ea commodo consequat. Duis autem vel eum iriure dolor in hendrerit in vulputate velit esse molestie consequat, vel illum dolore eu feugiat nulla facilisis at vero eros et accumsan et iusto odio dignissim qui blandit praesent luptatum zzril delenit augue duis dolore te feugait nulla facilisi.<br>At vero eos et accusam et justo duo dolores et ea rebum. Stet clita kasd gubergren, no sea takimata sanctus est Lorem ipsum dolor sit amet. Lorem ipsum dolor sit amet, consetetur sadipscing elitr, sed diam nonumy eirmod tempor invidunt ut labore et dolore magna aliquyam erat, sed diam voluptua. At vero eos et accusam et justo duo dolores et ea rebum. Stet clita kasd gubergren, no sea takimata sanctus est Lorem ipsum dolor sit amet, consetetur sadipscing elitr, At accusam aliquyam diam diam dolore dolores duo eirmod eos erat, et nonumy sed tempor et et invidunt justo labore Stet clita ea et gubergren, kasd magna no rebum. sanctus sea sed takimata ut vero voluptua. est Lorem ipsum dolor sit amet. Lorem ipsum dolor sit amet, consetetur</p>
      <p class="letter letter--closing">Mit freundlichen Grüßen</p>
      <p class="letter letter--signature">Max Mustermann<br>Beispielort, 31. Juli 2014</p>
      <div class="letter-footer-rule"></div>
      <div class="letter-footer">
        <div>Max Mustermann<br>Musterstraße 1<br>01234 Musterstadt</div>
        <div>Tel.: 012345 678<br>Fax: 01234567 99</div>
        <div>info@voskuhl-holz.de<br>www.voskuhl-holz.de</div>
        <div>Bankinstitut: Muster<br>IBAN: 440404304304443<br>BIC: 4323434343</div>
      </div>
      <div class="slate-bar"></div>
    </article>

    <article class="card card--front">
      <div class="gold-bar"></div>
      <div class="card__brand">
        <div class="wordmark">MARLEN VOSKUHL</div>
        <div class="tagline">EXCLUSIVE WOOD DESIGN</div>
      </div>
      <p class="card__name">Marlen Voskuhl</p>
      <p class="card__title">Titel / Bezeichnung</p>
      <p class="card__address">Kranichweg 14<br>28195 Weserhafen</p>
      <ul class="card__contacts">
        <li><svg viewBox="0 0 10 10"><path d="M2 1l2 2-1 1.5c.7 1.3 1.5 2.1 2.5 2.5L7 6l2 2-1.5 1.5C4 9 1 6 .5 2.5z" fill="#c98f3f"/></svg>0421/55 60 12</li>
        <li><svg viewBox="0 0 10 10"><rect x="1" y="3" width="8" height="6" fill="#c98f3f"/><rect x="3" y="1" width="4" height="3" fill="#c98f3f"/></svg>0421 / 55 60 19</li>
        <li><svg viewBox="0 0 10 10"><rect x="0.5" y="2" width="9" height="6" fill="#c98f3f"/><path d="M0.5 2l4.5 3.5L9.5 2" stroke="#fff" fill="none"/></svg>info@voskuhl-holz.de</li>
        <li><svg viewBox="0 0 10 10"><circle cx="5" cy="5" r="4.3" fill="none" stroke="#c98f3f" stroke-width="1.2"/><path d="M1 5h8M5 1v8" stroke="#c98f3f"/></svg>www.voskuhl-holz.de</li>
      </ul>
      <div class="slate-bar"></div>
    </article>

    <article class="card card--back">
      <div class="wordmark">MARLEN VOSKUHL</div>
    </article>
  </section>
</body>
</html>
```